Dravel

We are openıng one huntıng showroom in Riyadh? Saudi Arabia. Company name is "DRAVEL".
Our logo designed and we need Business Card Design now.
I attached DRAVEL logo below.
Front side will English and back side will be Arabic

```html
<!DOCTYPE html>
<html lang="en">
<head>
<meta charset="utf-8">
<title>Dravel Business Card</title>
<link rel="stylesheet" href="https://fonts.googleapis.com/css2?family=Cairo:wght@400;600;700&family=Open+Sans:wght@400;600;700&display=swap">
<style>
  :root {
    --stage: #2a2c2f;
    --card: #070707;
    --brand-green: #0f8c4f;
    --lime: #8db43b;
    --white: #f2f2f2;
    --muted: #d8d8d8;
  }
  * { margin: 0; padding: 0; box-sizing: border-box; }
  html, body { width: 1200px; height: 900px; overflow: hidden; }
  body {
    background: var(--stage);
    font-family: "Open Sans", Arial, sans-serif;
    display: flex;
    flex-direction: column;
    align-items: center;
    justify-content: center;
    gap: 46px;
  }
  .card {
    position: relative;
    width: 680px;
    height: 388px;
    background: var(--card);
    border-radius: 28px;
    overflow: hidden;
  }
  .card__band {
    position: absolute;
    left: 0; right: 0; bottom: 0;
    height: 24px;
    background: var(--brand-green);
  }
  .card__rule {
    position: absolute;
    top: 150px;
    height: 2px;
    background: var(--lime);
  }
  .card__rule::after {
    content: "";
    position: absolute;
    top: 0;
    width: 2px;
    height: 150px;
    background: var(--lime);
  }
  .holder { position: absolute; top: 44px; }
  .holder__name {
    color: var(--white);
    font-weight: 700;
    font-size: 27px;
    letter-spacing: 0.5px;
    line-height: 1.2;
  }
  .holder__title { color: var(--lime); font-size: 15px; line-height: 1.4; }
  .contacts {
    position: absolute;
    top: 170px;
    list-style: none;
    color: var(--muted);
    font-size: 15px;
  }
  .contacts li { display: flex; align-items: center; gap: 10px; height: 30px; }
  .contacts svg { width: 14px; height: 14px; flex: none; }
  .brand-name {
    position: absolute;
    top: 58px;
    color: var(--brand-green);
    font-family: "Open Sans", Arial, sans-serif;
    font-weight: 700;
    font-size: 64px;
    letter-spacing: 2px;
    line-height: 1;
  }
  .address {
    position: absolute;
    bottom: 52px;
    color: var(--white);
    font-size: 16px;
    line-height: 1.6;
    text-align: right;
  }

  /* front (English) */
  .card--front .holder { left: 44px; }
  .card--front .contacts { left: 44px; }
  .card--front .card__rule { left: 210px; right: 60px; }
  .card--front .card__rule::after { right: 0; }
  .card--front .brand-name { right: 60px; }
  .card--front .address { right: 80px; }

  /* back (Arabic) */
  .card--back { font-family: "Cairo", Arial, sans-serif; }
  .card--back .holder { right: 44px; text-align: right; }
  .card--back .holder__name { font-family: "Cairo", Arial, sans-serif; font-size: 26px; }
  .card--back .contacts { right: 44px; }
  .card--back .contacts li { flex-direction: row-reverse; }
  .card--back .card__rule { right: 210px; left: 60px; }
  .card--back .card__rule::after { left: 0; }
  .card--back .brand-name { left: 60px; }
  .card--back .address { left: 80px; right: auto; text-align: left; }
</style>
</head>
<body>

  <section class="card card--front" lang="en">
    <div class="holder">
      <p class="holder__name">YOUR NAME</p>
      <p class="holder__title">Job Title</p>
    </div>
    <div class="card__rule"></div>
    <ul class="contacts">
      <li>
        <svg viewBox="0 0 14 14"><rect width="14" height="14" rx="3" fill="#0f8c4f"/><path d="M4 3.5l1.5 0 .7 2-1 .8a5 5 0 0 0 2.5 2.5l.8-1 2 .7v1.5c-3.5.5-7-3-6.5-6.5z" fill="#070707"/></svg>
        000 000 0000
      </li>
      <li>
        <svg viewBox="0 0 14 14"><rect width="14" height="14" rx="3" fill="#0f8c4f"/><path d="M3 4.5h8v5H3z" fill="none" stroke="#070707" stroke-width="1.2"/><path d="M3 4.5l4 3 4-3" fill="none" stroke="#070707" stroke-width="1.2"/></svg>
        youremail@address
      </li>
      <li>
        <svg viewBox="0 0 14 14"><circle cx="7" cy="7" r="7" fill="#0f8c4f"/><circle cx="7" cy="7" r="4" fill="none" stroke="#070707" stroke-width="1.1"/><path d="M3 7h8M7 3v8" stroke="#070707" stroke-width="1.1"/></svg>
        www.yourwebsite.com
      </li>
    </ul>
    <p class="brand-name">DRAVEL</p>
    <p class="address">0000, Anywhere, Somewhere<br>Riyadh 0000</p>
    <div class="card__band"></div>
  </section>

  <section class="card card--back" lang="ar" dir="ltr">
    <div class="holder" dir="rtl">
      <p class="holder__name">الاسم الكامل</p>
      <p class="holder__title">عنوان وظيفي</p>
    </div>
    <div class="card__rule"></div>
    <ul class="contacts">
      <li>
        <svg viewBox="0 0 14 14"><rect width="14" height="14" rx="3" fill="#0f8c4f"/><path d="M4 3.5l1.5 0 .7 2-1 .8a5 5 0 0 0 2.5 2.5l.8-1 2 .7v1.5c-3.5.5-7-3-6.5-6.5z" fill="#070707"/></svg>
        <span dir="rtl">هاتف</span>
      </li>
      <li>
        <svg viewBox="0 0 14 14"><rect width="14" height="14" rx="3" fill="#0f8c4f"/><path d="M3 4.5h8v5H3z" fill="none" stroke="#070707" stroke-width="1.2"/><path d="M3 4.5l4 3 4-3" fill="none" stroke="#070707" stroke-width="1.2"/></svg>
        <span dir="rtl">البريد الالكتروني</span>
      </li>
      <li>
        <svg viewBox="0 0 14 14"><circle cx="7" cy="7" r="7" fill="#0f8c4f"/><circle cx="7" cy="7" r="4" fill="none" stroke="#070707" stroke-width="1.1"/><path d="M3 7h8M7 3v8" stroke="#070707" stroke-width="1.1"/></svg>
        <span dir="rtl">موقع الكتروني</span>
      </li>
    </ul>
    <p class="brand-name">DRAVEL</p>
    <p class="address" dir="rtl">عنوانك<br>الرياض ، البريد</p>
    <div class="card__band"></div>
  </section>

</body>
</html>
```